Web Design Project

Psychotherapist in Private Practice
Practice name "The Steady Harbor"
The population is professional adults seeking life coaching and change consultation
I am including a photo for inspiration ONLY - It includes the theme of light and tree branches. There does not HAVE to be a photograph . An illustration , concept or theme of nature /light / generativity / growth / creativity is acceptable
Clean sharp lines Light colors, minimalist , modern.
There is a separate project for a logo design that will become part of the web design
Here are examples of two logos/websites I like
http://www.quietrivergroup.example/
http://www.brightknollpartners.example/

Target Market(s)

Professional adults seeking life coaching

Industry/Entity Type

Life Coaching

Requirements
Should not have
• Although the business name has 'compassion' in it, designs with hearts in it would have to be pretty stylish, subtle, mature and sophisticated to be considered.

```html
<!DOCTYPE html>
<html lang="en">
<head>
<meta charset="utf-8">
<title>The Steady Harbor</title>
<link href="https://fonts.googleapis.com/css2?family=Mulish:wght@400;500;600;700&display=swap" rel="stylesheet">
<style>
:root{
  --green:#6a9f12;
  --green-dark:#4f7a0b;
  --green-text:#6f9a18;
  --ink:#2b2b2b;
  --body:#7a7a7a;
  --link:#3c86b5;
  --panel:#f1f1f1;
  --rule:#dcdcdc;
}
*{margin:0;padding:0;box-sizing:border-box}
html,body{width:1181px;height:1200px;overflow:hidden;background:#fff}
body{font-family:"Mulish",Arial,sans-serif;color:var(--body);position:relative}
.site-header{position:absolute;left:0;top:0;width:1181px;height:89px;background:linear-gradient(#fff,#f2f2f2)}
.brand{position:absolute;left:118px;top:14px;display:flex;align-items:center;gap:14px}
.brand-mark{width:56px;height:56px;border-radius:50%;background:var(--green)}
.brand-name{font-size:16px;font-weight:500;color:var(--ink);line-height:21px;text-transform:uppercase;letter-spacing:.2px}
.social{position:absolute;top:19px;left:943px;display:flex;gap:7px}
.social span{width:25px;height:25px;border:1px solid #cfcfcf;border-radius:3px;background:linear-gradient(#fff,#e6e6e6)}
.main-nav{position:absolute;top:61px;left:448px;display:flex;font-size:14px;color:#333}
.main-nav a{color:inherit;text-decoration:none;margin-right:25px;position:relative;height:28px}
.main-nav a.current{color:var(--green)}
.main-nav a.current::after{content:"";position:absolute;left:-2px;right:-2px;bottom:-1px;height:5px;background:#fff}
.main-nav a:last-child{margin-left:11px;margin-right:0}
.header-rule{position:absolute;top:89px;left:0;width:1181px;height:5px;background:var(--green-dark)}
.hero{position:absolute;top:94px;left:0;width:1181px;height:356px;background:linear-gradient(180deg,#6d9fcc 0%,#b9d2e6 40%,#c9b98a 62%,#9b8a3a 74%,#d19a2e 88%,#b9862d 100%)}
.hero-caption{position:absolute;left:118px;top:148px;width:354px;height:156px;background:rgba(40,40,30,.72)}
.hero-caption h2{height:37px;background:rgba(50,50,50,.9);border-bottom:2px solid rgba(255,255,255,.25);color:#fff;font-size:20px;font-weight:600;padding:4px 18px;text-transform:uppercase}
.hero-caption p{color:#e8e8e8;font-size:12px;line-height:19px;padding:7px 18px 0}
.btn{display:inline-block;background:linear-gradient(#7cb51f,#5b8e0d);color:#fff;text-decoration:none}
.hero-caption .btn{margin:11px 0 0 18px;font-size:13px;padding:5px 7px}
.ask{position:absolute;top:460px;left:0;width:1181px;height:135px;background:repeating-linear-gradient(45deg,#f7f7f7 0 2px,#fdfdfd 2px 4px);border-bottom:1px solid var(--rule)}
.ask h3{position:absolute;left:118px;top:12px;font-size:19px;font-weight:500;color:var(--ink)}
.ask-photo{position:absolute;left:118px;top:42px;width:87px;height:77px;background:linear-gradient(135deg,#8a6b52,#a9b6c9 60%,#5a6a86)}
.ask p{position:absolute;left:216px;top:44px;width:700px;font-size:12px;line-height:19px}
.ask .btn{position:absolute;left:941px;top:55px;width:124px;height:39px;font-size:16px;font-weight:600;line-height:39px;text-align:center;border:1px solid #4f7a0b}
.content{position:absolute;top:596px;left:118px;width:600px}
.content h1{font-size:23px;font-weight:500;color:var(--ink);margin-top:17px}
.content .lede{font-size:18px;color:var(--green-text);margin:7px 0 6px -1px}
.content p{font-size:12.5px;line-height:19.7px;margin-bottom:14px}
.content blockquote{font-size:18px;color:var(--ink);line-height:24.5px;margin:-1px 0 2px}
.sidebar{position:absolute;top:596px;left:736px;width:328px;height:554px;background:var(--panel)}
.video{position:absolute;left:24px;top:21px;width:279px;height:198px}
.video h3{height:33px;background:linear-gradient(#7cb51f,#5c8f0d);color:#fff;font-size:18px;font-weight:600;padding:4px 8px}
.video-frame{position:relative;height:165px;background:linear-gradient(180deg,#3d3a34,#8a6a32 55%,#2a2a26)}
.play{position:absolute;left:128px;top:48px}
.side-block{position:absolute;left:24px;width:285px;font-size:11px;line-height:17px}
.side-block h4{font-size:13.5px;font-weight:600;color:var(--ink);margin-bottom:5px}
.side-block .title{font-size:13.5px;font-weight:600;color:var(--green-text);line-height:19px;margin-bottom:5px}
.side-block a{color:var(--link);text-decoration:none;font-size:12px}
.side-rule{position:absolute;left:24px;width:285px;height:1px;background:var(--rule)}
.calendar{display:flex;align-items:center;gap:14px}
.site-footer{position:absolute;top:1150px;left:0;width:1181px;height:50px;background:linear-gradient(#3a3a3a,#050505);border-top:1px solid #555;color:#fff;font-size:12px}
.footer-nav{position:absolute;left:119px;top:17px;display:flex;gap:17px}
.footer-nav span:last-child{margin-left:9px}
.copyright{position:absolute;right:118px;top:17px}
</style>
</head>
<body>
<header class="site-header">
  <div class="brand"><span class="brand-mark"></span><span class="brand-name">The<br>Steady Harbor</span></div>
  <div class="social"><span></span><span></span><span></span><span></span></div>
  <nav class="main-nav">
    <a class="current" href="#">Home</a><a href="#">Meet Our Team</a><a href="#">Therapy &amp; Training</a><a href="#">Multimedia</a><a href="#">Schedule &amp; Fees</a><a href="#">Contact Us</a>
  </nav>
</header>
<div class="header-rule"></div>
<section class="hero" role="img" aria-label="Open road leading through golden fields toward mountains under a blue sky">
  <div class="hero-caption">
    <h2>Lorem ipsum dolor sit amet</h2>
    <p>Sed ut perspiciatis unde omnis iste natus error sit volup-tatem accusantium doloremque laudantium, totam rem aperiam.</p>
    <a class="btn" href="#">View Detail</a>
  </div>
</section>
<section class="ask">
  <h3>Ask Dr Elliot Harwell</h3>
  <div class="ask-photo" role="img" aria-label="Portrait of the therapist"></div>
  <p>Sed ut perspiciatis unde omnis iste natus error sit voluptatem accusantium doloremque laudantium, totam rem aperiam, eaque ipsa quae ab illo inventore veritatis et quasi architecto beatae vitae dicta sunt explicabo. Nemo enim ipsam volupta-tem quia voluptas sit aspernatur aut odit aut fugit, sed quia consequuntur magni dolores eos qui ratione voluptatem sequi nesciunt.</p>
  <a class="btn" href="#">Ask A Doctor</a>
</section>
<main class="content">
  <h1>Welcome To The Steady Harbor</h1>
  <p class="lede">Lorem ipsum dolor sit amet, consectetur adipisicing elit,</p>
  <p>Lorem ipsum dolor sit amet, consectetur adipisicing elit, sed do eiusmod tempor incididunt ut labore et dolore magna aliqua. Ut enim ad minim veniam, quis nostrud exercitation ullamco laboris nisi ut aliquip ex ea commodo consequat.</p>
  <p>Duis aute irure dolor in reprehenderit in voluptate velit esse cillum dolore eu fugiat nulla pariatur. Excepteur sint occaecat cupidatat non proident, sunt in culpa qui officia deserunt mollit anim id est laborum.Lorem ipsum dolor sit amet, consectetur adipisicing elit, sed do eiusmod tempor incididunt ut labore et dolore magna aliqua. Ut enim ad minim veniam, quis nostrud exercitation ullamco laboris nisi ut aliquip ex ea commodo consequat.</p>
  <blockquote>“At vero eos et accusamus et iusto odio dignissimos ducimus qui blanditiis praesentium voluptatum”</blockquote>
  <p>Lorem ipsum dolor sit amet, consectetur adipisicing elit, sed do eiusmod tempor incididunt ut labore et dolore magna aliqua. Ut enim ad minim veniam, quis nostrud exercitation ullamco laboris nisi ut aliquip ex ea commodo consequat. Duis aute irure dolor in reprehenderit in voluptate velit esse cillum dolore eu fugiat nulla pariatur.</p>
  <p>Excepteur sint occaecat cupidatat non proident, sunt in culpa qui officia deserunt mollit anim id est laborum.Lorem ipsum dolor sit amet, consectetur adipisicing elit, sed do eiusmod tempor incididunt ut labore et dolore magna aliqua. Ut enim ad minim veniam, quis nostrud exercitation ullamco laboris nisi ut aliquip ex ea commodo consequat. Lorem ipsum dolor sit amet, consectetur adipisicing elit, sed do eiusmod tempor incididunt ut labore et dolore magna aliqua. Ut enim ad minim veniam, quis nostrud exercitation ullamco laboris nisi ut aliquip ex ea commodo consequat.</p>
</main>
<aside class="sidebar">
  <div class="video">
    <h3>Our Video</h3>
    <div class="video-frame" role="img" aria-label="Video still of a road at sunset beside a lake with a lone tree">
      <svg class="play" width="24" height="38" viewBox="0 0 24 38"><path d="M0 0L24 19L0 38Z" fill="rgba(255,255,255,.6)"/></svg>
    </div>
  </div>
  <div class="side-block" style="top:250px">
    <h4>Upcoming Workshop:</h4>
    <div class="title">Introduction To Compassionate</div>
    <p>Lorem ipsum dolor sit amet, consectetur adipisicing elit, sed do eiusmod tempor incididunt ut labore et dolore magna aliqua.</p>
  </div>
  <div class="side-rule" style="top:346px"></div>
  <div class="side-block" style="top:354px">
    <h4>Blog</h4>
    <div class="title">Compassionate Training Can Make You Happier</div>
    <a href="#">Read this post</a> - <a href="#">See all posts</a>
  </div>
  <div class="side-rule" style="top:443px"></div>
  <div class="side-block" style="top:456px">
    <h4>2013 Calendar</h4>
    <div class="calendar">
      <svg width="46" height="48" viewBox="0 0 46 48"><rect x="2" y="6" width="42" height="40" rx="3" fill="#f4f4f4" stroke="#bbb"/><rect x="2" y="6" width="42" height="12" rx="3" fill="#d9342b"/><g fill="#999"><rect x="8" y="23" width="6" height="4"/><rect x="17" y="23" width="6" height="4"/><rect x="26" y="23" width="6" height="4"/><rect x="35" y="23" width="5" height="4"/><rect x="8" y="30" width="6" height="4"/><rect x="17" y="30" width="6" height="4"/><rect x="26" y="30" width="6" height="4"/><rect x="35" y="30" width="5" height="4"/><rect x="8" y="37" width="6" height="4"/><rect x="17" y="37" width="6" height="4"/><rect x="26" y="37" width="6" height="4"/></g><g fill="#888"><rect x="10" y="2" width="3" height="8" rx="1"/><rect x="21" y="2" width="3" height="8" rx="1"/><rect x="32" y="2" width="3" height="8" rx="1"/></g></svg>
      <a href="#">See our Calendar of<br>Courses &amp; Events</a>
    </div>
  </div>
  <div class="side-rule" style="top:538px"></div>
</aside>
<footer class="site-footer">
  <div class="footer-nav"><span>Home</span><span>Meet Our Team</span><span>Therapy &amp; Training</span><span>Multimedia</span><span>Schedule &amp; Fees</span><span>Contact Us</span></div>
  <div class="copyright">Copyright © 2013 All Rights Reserved.</div>
</footer>
</body>
</html>
```